E-Book/ Buch-Cover spannenden Liebesroman gesucht.
Zielgruppe
Ich bin Autorin und suche ein ansprechendes Cover für mein E-Book mit dem Titel:
' Schattenhafte Reue'. Es handelt sich um einen spannenden Liebesroman. Die emotionalen Ängste des Protagonisten, stehen neben den offensichtlichen Bedrohungen der Hauptfigur. Beide müssen ihren Weg zu einem Happyend finden. Da der Titel schon etwas „schreit“, sollte das Cover diesen Eindruck eventuell etwas abfedern.
Aufgabenstellung
Kein Kitsch, kein Schnulzencover, es handelt sich bei aller Dramatik trotzdem um einen Liebesroman. Keinen Thriller.

```html
<!DOCTYPE html>
<html lang="de">
<head>
<meta charset="utf-8">
<title>Schattenhafte Reue – Cover</title>
<link rel="stylesheet" href="https://fonts.googleapis.com/css2?family=Montserrat:wght@700&family=Josefin+Sans:wght@400&display=swap">
<style>
  :root {
    --sky-deep: #0f2a7a;
    --sky-mid: #2f5fc4;
    --sky-light: #9fc3ea;
    --glow: #f3ead0;
    --floor: #0b0f1c;
    --title-white: #ffffff;
    --accent-red: #e3173f;
    --imprint-black: #0a0a0a;
  }
  html, body {
    margin: 0;
    padding: 0;
    width: 815px;
    height: 1200px;
    overflow: hidden;
    background: #ffffff;
  }
  .cover {
    position: relative;
    width: 815px;
    height: 1200px;
    overflow: hidden;
    background: var(--sky-deep);
  }
  .cover-scene {
    position: absolute;
    inset: 0;
    background:
      radial-gradient(ellipse 260px 200px at 300px 560px, var(--glow) 0%, rgba(243,234,208,0.6) 30%, rgba(159,195,234,0) 100%),
      radial-gradient(ellipse 520px 420px at 330px 540px, var(--sky-light) 0%, rgba(47,95,196,0.8) 45%, rgba(15,42,122,0) 100%),
      radial-gradient(ellipse 220px 420px at 690px 800px, rgba(10,16,40,0.85) 0%, rgba(10,16,40,0) 100%),
      linear-gradient(180deg, #1a3fa6 0%, var(--sky-mid) 40%, #1d3c8e 75%, var(--sky-deep) 100%);
  }
  .cover-floor {
    position: absolute;
    left: 0;
    right: 0;
    bottom: 0;
    height: 270px;
    background: linear-gradient(180deg, #1d2a4e 0%, #121a33 30%, var(--floor) 100%);
  }
  .author {
    position: absolute;
    top: 205px;
    right: 50px;
    margin: 0;
    font-family: "Josefin Sans", sans-serif;
    font-weight: 400;
    font-size: 40px;
    color: var(--title-white);
    letter-spacing: 0.5px;
  }
  .title-rule {
    position: absolute;
    left: 76px;
    top: 420px;
    width: 12px;
    height: 700px;
    background: var(--title-white);
  }
  .title {
    position: absolute;
    left: 12px;
    top: 318px;
    margin: 0;
    font-family: "Montserrat", sans-serif;
    font-weight: 700;
    font-size: 112px;
    line-height: 100px;
    color: var(--title-white);
    text-transform: uppercase;
    letter-spacing: -2px;
  }
  .title-line {
    display: block;
    padding-left: 100px;
    white-space: nowrap;
    text-shadow: 0 2px 6px rgba(0,0,0,0.35);
  }
  .title-line.lead {
    padding-left: 0;
  }
  .title-line.lead .initial {
    display: inline-block;
    width: 100px;
    text-align: right;
  }
  .initial {
    color: var(--accent-red);
  }
  .genre {
    position: absolute;
    left: 412px;
    top: 845px;
    margin: 0;
    font-family: "Josefin Sans", sans-serif;
    font-size: 38px;
    color: var(--title-white);
  }
  .imprint {
    position: absolute;
    left: 372px;
    top: 1055px;
    width: 52px;
    height: 120px;
    background: var(--imprint-black);
    display: flex;
    align-items: center;
    justify-content: center;
  }
  .imprint-name {
    font-family: "Josefin Sans", sans-serif;
    font-size: 16px;
    color: var(--title-white);
    writing-mode: vertical-rl;
    letter-spacing: 1px;
  }
</style>
</head>
<body>
  <main class="cover">
    <div class="cover-scene" role="img" aria-label="Stimmungsfoto: stürmischer blauer Himmel mit Blitz und hellem Lichtschein, rechts eine sitzende Frau als Silhouette, die sich in Rauch auflöst"></div>
    <div class="cover-floor" aria-hidden="true"></div>

    <p class="author">j.a. sternfeld</p>

    <div class="title-rule" aria-hidden="true"></div>
    <h1 class="title" aria-label="Schattenhafte Reue">
      <span class="title-line lead"><span class="initial">S</span>CHAT</span>
      <span class="title-line">TEN</span>
      <span class="title-line">HAF</span>
      <span class="title-line">TE</span>
      <span class="title-line"><span class="initial">R</span>EUE</span>
    </h1>
    <p class="genre">roman</p>

    <div class="imprint">
      <span class="imprint-name">lerche</span>
    </div>
  </main>
</body>
</html>
```